I need a business card design for my new clinic (SPORTS MEDICINE OF KNEE). I am orthopedist, expert in sports surgery, especially knee surgery. I prefer, as colors, the colors of my logo (green, black and white). I already have my logo and should appear on my card. It's good to see my site to have ideas (www.drlucianovarela.com)
It needs contain:
my name: Dr. Luciano Varela
my registration: CRM 584-902
my specialty: Cirurgia do Joelho / Esporte
my address: Centro Executivo - Pinheiral Plaza
Av. Doutor Augusto Brandão Cunha, 2740 sala 0836
Jd. Ipanema - Ribeirão Preto - SP
my phone number: Tel (16) 8245-3908
my clinic phone: (16) 3670-4851
my e-mail: drlucianovarela@mailbox-exemplo.com
my site: www.drlucianovarela.com

Target Market(s)

futures patients

Industry/Entity Type

Clinic

Requirements
Nice to have
• letters not overfilled
straight lines, with few curves

```html
<!DOCTYPE html>
<html lang="pt-BR">
<head>
<meta charset="utf-8">
<title>Dr. Luciano Varela — Cartão de Visita</title>
<link href="https://fonts.googleapis.com/css2?family=Cinzel:wght@400;600&family=Open+Sans:wght@400;600;700&display=swap" rel="stylesheet">
<style>
  :root{
    --backdrop:#e4ddd0;
    --paper:#f4f4f1;
    --ink:#1d1d1d;
    --ink-soft:#3a3a3a;
    --slate:#2a2c2d;
    --slate-deep:#1b1c1d;
    --band:#6f716d;
    --band-ink:#1e1f1f;
    --green:#5fbf57;
    --mint:#a6e3a0;
    --mark-grey:#5a5c5d;
    --silver:#d7d9d8;
  }
  *{margin:0;padding:0;box-sizing:border-box}
  html,body{width:1200px;height:1000px;overflow:hidden}
  body{
    background:var(--backdrop);
    font-family:"Open Sans",Arial,sans-serif;
    display:flex;flex-direction:column;align-items:center;justify-content:center;gap:56px;
  }
  .card{
    width:660px;height:378px;position:relative;overflow:hidden;
    box-shadow:0 10px 28px rgba(0,0,0,.22);
  }

  /* Front: dark side */
  .card--front{
    background:radial-gradient(ellipse at 40% 35%, #3a3c3d 0%, var(--slate) 45%, var(--slate-deep) 100%);
  }
  .brand{
    position:absolute;left:150px;top:78px;display:flex;align-items:center;gap:22px;
  }
  .brand__square{
    width:78px;height:70px;background:var(--green);border-radius:8px;flex:none;
  }
  .brand__text{display:flex;flex-direction:column}
  .brand__name{
    font-family:"Cinzel",Georgia,serif;font-weight:600;font-size:70px;line-height:1;
    color:var(--silver);letter-spacing:2px;
  }
  .brand__tagline{
    font-family:"Cinzel",Georgia,serif;font-weight:400;font-size:19px;
    color:var(--green);letter-spacing:1px;margin-top:6px;margin-left:4px;
  }
  .contact-band{
    position:absolute;left:0;right:0;bottom:36px;height:46px;
    background:linear-gradient(180deg,#7a7c78,var(--band));
    display:flex;align-items:center;justify-content:center;gap:26px;
    font-size:13px;color:var(--band-ink);letter-spacing:.2px;
  }

  /* Back: white side */
  .card--back{background:var(--paper)}
  .doctor{position:absolute;left:300px;top:44px}
  .doctor__name{font-weight:700;font-size:27px;color:var(--ink)}
  .doctor__line{font-weight:600;font-size:14px;color:var(--ink-soft);line-height:1.4;margin-left:4px}
  .doctor__line--first{margin-top:4px}
  .phones{position:absolute;left:44px;top:160px;font-weight:600;font-size:14px;color:var(--ink-soft);line-height:1.5}
  .address{position:absolute;left:44px;top:226px;font-weight:700;font-size:14px;color:var(--ink);line-height:1.45;width:340px}
  .back-brand{
    position:absolute;right:34px;bottom:40px;display:flex;align-items:center;gap:12px;
  }
  .back-brand__square{width:150px;height:134px;background:var(--mark-grey);border-radius:14px}
</style>
</head>
<body>

  <section class="card card--front" aria-label="Frente do cartão">
    <div class="brand">
      <div class="brand__square"></div>
      <div class="brand__text">
        <span class="brand__name">VARELA</span>
        <span class="brand__tagline">Traumatologia Esportiva</span>
      </div>
    </div>
    <div class="contact-band">
      <span>e-mail: drlucianovarela@mailbox-exemplo.com</span>
      <span>site: www.drlucianovarela.com</span>
    </div>
  </section>

  <section class="card card--back" aria-label="Verso do cartão">
    <div class="doctor">
      <h1 class="doctor__name">Dr. Luciano Varela</h1>
      <p class="doctor__line doctor__line--first">Ortopedista</p>
      <p class="doctor__line">Cirurgia do Joelho / Esporte</p>
      <p class="doctor__line">registration: CRM 584-902</p>
    </div>
    <div class="phones">
      <p>phone number: Tel (16) 8245-3908</p>
      <p>clinic phone: (16) 3670-4851</p>
    </div>
    <address class="address" style="font-style:normal">
      Centro Executivo - Pinheiral Plaza Av. Doutor Augusto Brandão Cunha, 2740 sala 0836 Jd. Ipanema - Ribeirão Preto - SP
    </address>
    <div class="back-brand">
      <div class="back-brand__square"></div>
    </div>
  </section>

</body>
</html>
```